Tarvel Ridge LLC

Need Professional Business cards for New Investment Fund

Target Market(s)

High Quality investors

Industry/Entity Type

Financial

Contact Information for Business Card

Phone Number +1 555 284 6193
Name Pavel Orlinsky
Title Fund Manager
email po@FundTarvel.example
Website www.FundTarvel.example

Colors

Designer to choose colors to be used in the design.

Requirements
Must have
• Must have our Logo and all of the above. Must be made so lettering and loge can be raised

```html
<!DOCTYPE html>
<html lang="en">
<head>
<meta charset="utf-8">
<title>Tarvel Ridge LLC – Business Card</title>
<link rel="stylesheet" href="https://fonts.googleapis.com/css2?family=EB+Garamond:wght@500;600;700&display=swap">
<style>
  :root {
    --backdrop: #e3dfdd;
    --card-white: #f7f7f7;
    --brand-green: #4fd03d;
    --deep-green: #3a4536;
    --ink-dark: #2f3a2c;
    --pattern-grey: #ececec;
    --text-light: #ffffff;
  }
  * { box-sizing: border-box; margin: 0; padding: 0; }
  html, body {
    width: 1200px; height: 901px; overflow: hidden;
    background: var(--backdrop);
    font-family: "EB Garamond", Georgia, serif;
  }
  .card-sheet {
    position: relative; width: 1200px; height: 901px;
    display: flex; align-items: center; justify-content: center; gap: 60px;
  }
  .card {
    position: relative; width: 530px; height: 303px;
    background: var(--card-white); overflow: hidden;
    box-shadow: 0 8px 22px rgba(0,0,0,0.16);
  }
  .card-front .shapes { position: absolute; inset: 0; }
  .holder { position: absolute; left: 36px; top: 44px; color: var(--text-light); }
  .holder-name { font-size: 27px; font-weight: 700; letter-spacing: 0.3px; white-space: nowrap; }
  .holder-title { font-size: 14px; font-weight: 600; margin-top: 2px; }
  .brand-name {
    position: absolute; right: 40px; top: 112px;
    font-size: 26px; font-weight: 700; color: var(--ink-dark); letter-spacing: 0.5px;
    white-space: nowrap;
  }
  .contact-band {
    position: absolute; left: 205px; right: 0; bottom: 0; height: 56px;
    display: flex; align-items: center; gap: 16px; padding-left: 18px;
    color: var(--text-light); font-size: 13px; font-weight: 500;
    white-space: nowrap;
  }
  .contact-item { display: flex; align-items: center; gap: 6px; }
  .contact-icon { width: 16px; height: 14px; flex: none; }
  .pattern-field {
    position: absolute; inset: 0; background: var(--pattern-grey);
  }
  .back-content {
    position: absolute; inset: 0; display: flex; flex-direction: column;
    align-items: center; justify-content: center; gap: 10px;
    color: var(--ink-dark);
  }
  .back-brand { font-size: 32px; font-weight: 700; letter-spacing: 0.6px; }
  .back-website { font-size: 14px; font-weight: 500; letter-spacing: 0.4px; }
</style>
</head>
<body>
<main class="card-sheet">
  <section class="card card-front" aria-label="Business card front">
    <svg class="shapes" viewBox="0 0 530 303" width="530" height="303" aria-hidden="true">
      <rect x="0" y="247" width="530" height="56" fill="var(--deep-green)"/>
      <polygon points="0,0 364,0 0,278" fill="var(--brand-green)"/>
      <line x1="364" y1="0" x2="0" y2="278" stroke="var(--card-white)" stroke-width="3"/>
      <polygon points="0,282 205,125 205,303 0,303" fill="var(--deep-green)"/>
    </svg>
    <div class="holder">
      <p class="holder-name">Pavel Orlinsky</p>
      <p class="holder-title">Fund Manager</p>
    </div>
    <p class="brand-name">Tarvel Ridge</p>
    <div class="contact-band">
      <span class="contact-item">
        <svg class="contact-icon" viewBox="0 0 17 15" aria-hidden="true">
          <rect width="17" height="15" rx="2" fill="var(--brand-green)"/>
          <path d="M4 10 q0-4 4.5-4 q4.5 0 4.5 4 z" fill="var(--card-white)"/>
          <rect x="3" y="4" width="11" height="2" rx="1" fill="var(--card-white)"/>
        </svg>
        +1 555 284 6193
      </span>
      <span class="contact-item">
        <svg class="contact-icon" viewBox="0 0 17 15" aria-hidden="true">
          <rect width="17" height="15" rx="2" fill="var(--brand-green)"/>
          <path d="M3 4 L8.5 8.5 L14 4 M3 11 L7 7.5 M14 11 L10 7.5" stroke="var(--card-white)" stroke-width="1.3" fill="none"/>
        </svg>
        po@FundTarvel.example
      </span>
    </div>
  </section>

  <section class="card card-back" aria-label="Business card back">
    <div class="pattern-field" role="img" aria-label="Faint repeating brand pattern background"></div>
    <div class="back-content">
      <p class="back-brand">Tarvel Ridge</p>
      <p class="back-website">www.FundTarvel.example</p>
    </div>
  </section>
</main>
</body>
</html>
```